THE POINT AT MAPLE SWALE HUDSON RIVER WATERFRONT LAND

crisp clear business cards on wood stock or thick paper with large font with a river otter logo, PERSONAL INFO ON ONE SIDE, PROJECT INFO ON THE OTHER SIDE
Updates

I don’t have a logo. Just thought that a photo of a river otter would look appealing.

Target Market(s)

Buyers and realtors

Industry/Entity Type

Real Estate Development

Contact Information for Business Card

MARTIN OSGOOD
518-730-4862 (Call or Text)
STONE HAVEN LLC PRINCIPAL

MOSHAVENRD@TARNMAIL.COM

Font styles to use
Sans Serif

Colors
fbfdfe
0792cd
00a990
fbed22
ec1f27

Requirements
Must have
• LARGE FONT, ROUNDED EDGES,
Nice to have
• ON THE BACK SIDE :
• THE POINT AT MAPLE SWALE
• HUDSON RIVER WATERFRONT LAND
• 2 TO 67 ACRES---READY TO BUILD
• PRICED TO SELL!

```html
<!DOCTYPE html>
<html lang="en">
<head>
<meta charset="utf-8">
<title>Stone Haven LLC — Business Card</title>
<link href="https://fonts.googleapis.com/css2?family=Work+Sans:wght@400;500&display=swap" rel="stylesheet">
<style>
  :root {
    --page: #e9ecef;
    --card-white: #fbfdfe;
    --brand-blue: #0792cd;
    --deep-blue: #0b6fa8;
    --rule-blue: #3aa8dc;
    --ink: #3c3f44;
    --muted: #6b6f75;
    --back-text: #e4ecf2;
  }
  * { box-sizing: border-box; margin: 0; padding: 0; }
  html, body { width: 1200px; height: 900px; overflow: hidden; }
  body {
    background: var(--page);
    font-family: "Work Sans", Arial, sans-serif;
    display: flex;
    flex-direction: column;
    align-items: center;
    justify-content: center;
    gap: 44px;
  }
  .card {
    width: 660px;
    height: 377px;
    border-radius: 14px;
    position: relative;
    overflow: hidden;
    box-shadow: 0 6px 18px rgba(0,0,0,0.18);
  }

  /* Front */
  .card-front {
    background: radial-gradient(circle at 62% 62%, #ffffff 0%, var(--card-white) 45%, #e7e9eb 100%);
  }
  .person { position: absolute; left: 40px; top: 70px; }
  .person-name {
    color: var(--brand-blue);
    font-size: 30px;
    font-weight: 500;
    letter-spacing: -0.5px;
  }
  .person-title { color: var(--muted); font-size: 17px; margin-top: 2px; }
  .divider {
    position: absolute;
    left: 40px; top: 152px;
    width: 450px; height: 2px;
    background: var(--rule-blue);
  }
  .contact {
    position: absolute; left: 40px; top: 172px;
    list-style: none;
    color: var(--ink);
    font-size: 17px;
    line-height: 1.55;
  }
  .contact li { display: flex; align-items: center; gap: 9px; }
  .contact svg { width: 13px; height: 13px; flex: none; }
  .brand-name {
    position: absolute; right: 48px; top: 118px;
    color: var(--brand-blue);
    font-size: 26px;
    font-weight: 500;
    letter-spacing: 1.5px;
  }
  .address {
    position: absolute; left: 300px; top: 200px;
    color: var(--ink);
    font-size: 18px;
    line-height: 1.35;
    font-style: normal;
  }

  /* Back */
  .card-back {
    background: linear-gradient(160deg, var(--brand-blue) 0%, var(--deep-blue) 100%);
    display: flex;
    flex-direction: column;
    align-items: center;
    justify-content: center;
    text-align: center;
    color: var(--back-text);
  }
  .back-brand {
    font-size: 48px;
    font-weight: 500;
    letter-spacing: 4px;
    margin-bottom: 26px;
  }
  .project-lines {
    font-size: 15px;
    letter-spacing: 1.2px;
    line-height: 1.7;
  }
</style>
</head>
<body>
  <section class="card card-front" aria-label="Card front">
    <div class="person">
      <h1 class="person-name">MARTIN OSGOOD</h1>
      <p class="person-title">Principal</p>
    </div>
    <div class="divider"></div>
    <ul class="contact">
      <li>
        <svg viewBox="0 0 24 24" aria-hidden="true"><path fill="#0792cd" d="M6.6 10.8a15.1 15.1 0 0 0 6.6 6.6l2.2-2.2a1 1 0 0 1 1-.25 11.4 11.4 0 0 0 3.6.57 1 1 0 0 1 1 1V20a1 1 0 0 1-1 1A17 17 0 0 1 3 4a1 1 0 0 1 1-1h3.5a1 1 0 0 1 1 1c0 1.25.2 2.45.57 3.57a1 1 0 0 1-.25 1z"/></svg>
        518-730-4862
      </li>
      <li>
        <svg viewBox="0 0 24 24" aria-hidden="true"><rect x="3" y="5" width="18" height="14" rx="2" fill="none" stroke="#0792cd" stroke-width="2"/><path d="M3 7l9 6 9-6" fill="none" stroke="#0792cd" stroke-width="2"/></svg>
        moshavenrd@tarnmail.com
      </li>
    </ul>
    <div class="brand-name">STONE HAVEN LLC</div>
    <address class="address">218b Ferry Lane,<br>Rivermark, NY, 12803</address>
  </section>

  <section class="card card-back" aria-label="Card back">
    <div class="back-brand">STONE HAVEN LLC</div>
    <p class="project-lines">
      THE POINT AT MAPLE SWALE | HUDSON RIVER WATERFRONT LAND<br>
      2 TO 67 ACRES---READY TO BUILD &nbsp;| PRICED TO SELL!
    </p>
  </section>
</body>
</html>
```